Awesome Business Card Design needed!

Hey there.
I'm looking for a simple but awesome business card design.
Type of company: Online advertisement agency
(please don't use the typical business people or statistics images on the card)
The front has to display the business name
and possibly some sort of logo ( perhaps something with the two M's of the biz name )
And the back of the card should say:
Name
Phone
Email
Let your imagination flow.
here are some designs that I like and that you can use as inspiration.
Simple but Awesome
http://images.pixelvantor.net/designs/55128_877673_43091_thumbnail.jpg
http://images.pixelvantor.net/designs/37714_747642_40106_image.jpg
http://images.pixelvantor.net/designs/55128_877673_43091_image.jpg
http://images.pixelvantor.net/designs/51321_781878_43091_image.jpg
http://images.pixelvantor.net/designs/33378_399063_15912_image.jpg
http://images.pixelvantor.net/designs/2337_271604_9495_image.jpg
good luck

```html
<!DOCTYPE html>
<html lang="en">
<head>
<meta charset="utf-8">
<title>Verlowe Media – Business Card</title>
<link rel="stylesheet" href="https://fonts.googleapis.com/css2?family=EB+Garamond:wght@400;500&family=Open+Sans:wght@400&display=swap">
<style>
  :root {
    --page-bg: #ecebe8;
    --card-black: #080909;
    --gloss-grey: #323434;
    --teal: #1d9cbd;
    --teal-light: #7fd3e6;
    --text-grey: #c9cccd;
    --text-soft: #e6e8e8;
  }
  * { box-sizing: border-box; margin: 0; padding: 0; }
  html, body {
    width: 1200px;
    height: 900px;
    overflow: hidden;
    background: var(--page-bg);
  }
  .sheet {
    position: relative;
    width: 1200px;
    height: 900px;
  }
  .card {
    position: absolute;
    left: 280px;
    width: 640px;
    height: 366px;
    border-radius: 26px;
    background: var(--card-black);
    overflow: hidden;
    box-shadow: 0 10px 26px rgba(0, 0, 0, 0.28);
  }
  .card--front { top: 66px; }
  .card--back { top: 468px; }

  .card__gloss {
    position: absolute;
    inset: 0;
    width: 100%;
    height: 100%;
  }

  .brand {
    position: absolute;
    font-family: "EB Garamond", serif;
  }
  .brand__name {
    font-weight: 500;
    color: var(--teal-light);
    letter-spacing: 0.04em;
    text-transform: uppercase;
    line-height: 1;
  }
  .brand__tagline {
    color: var(--text-grey);
    letter-spacing: 0.03em;
    margin-top: 6px;
  }

  .card--front .brand {
    left: 0;
    right: 0;
    top: 158px;
    text-align: center;
  }
  .card--front .brand__name { font-size: 46px; }
  .card--front .brand__tagline { font-size: 22px; }

  .card--back .brand {
    left: 46px;
    top: 214px;
  }
  .card--back .brand__name { font-size: 34px; }
  .card--back .brand__tagline { font-size: 18px; }

  .holder {
    position: absolute;
    left: 360px;
    top: 62px;
    font-family: "EB Garamond", serif;
  }
  .holder__name {
    font-size: 30px;
    color: var(--teal);
    line-height: 1;
  }
  .holder__position {
    font-size: 17px;
    color: var(--text-grey);
    margin-top: 4px;
  }

  .contacts {
    position: absolute;
    left: 360px;
    top: 160px;
    list-style: none;
    font-family: "Open Sans", sans-serif;
    font-size: 14px;
    color: var(--text-soft);
  }
  .contacts__item {
    display: flex;
    align-items: center;
    gap: 12px;
    margin-bottom: 14px;
  }
  .contacts__icon { width: 16px; height: 16px; flex: none; }

  .card__stripe {
    position: absolute;
    left: 0;
    right: 0;
    bottom: 0;
    height: 18px;
    background: var(--teal);
  }
  .card__stripe-tip {
    position: absolute;
    right: 0;
    bottom: 0;
    width: 48px;
    height: 18px;
    background: var(--teal-light);
  }
</style>
</head>
<body>
<main class="sheet">

  <section class="card card--front" aria-label="Card front">
    <svg class="card__gloss" viewBox="0 0 640 366" preserveAspectRatio="none" aria-hidden="true">
      <path d="M0 0 H470 Q300 170 0 300 Z" fill="var(--gloss-grey)"/>
    </svg>
    <div class="brand">
      <p class="brand__name">Verlowe Media</p>
      <p class="brand__tagline">Online advertisement agency</p>
    </div>
  </section>

  <section class="card card--back" aria-label="Card back">
    <div class="brand">
      <p class="brand__name">Verlowe Media</p>
      <p class="brand__tagline">Online advertisement agency</p>
    </div>

    <div class="holder">
      <p class="holder__name">Your Name</p>
      <p class="holder__position">Company Position</p>
    </div>

    <ul class="contacts">
      <li class="contacts__item">
        <svg class="contacts__icon" viewBox="0 0 16 16" aria-hidden="true">
          <rect x="1" y="3" width="14" height="10" fill="var(--teal)"/>
          <path d="M1 3 L8 9 L15 3" fill="none" stroke="var(--card-black)" stroke-width="1.2"/>
        </svg>
        <span>name@domainname.com</span>
      </li>
      <li class="contacts__item">
        <svg class="contacts__icon" viewBox="0 0 16 16" aria-hidden="true">
          <path d="M4 1.5 L6.5 4.5 L5 6.5 Q6.5 9.5 9.5 11 L11.5 9.5 L14.5 12 L12.5 14.5 Q5 14 1.5 3.5 Z" fill="var(--teal)"/>
        </svg>
        <span>000 000 0000</span>
      </li>
    </ul>

    <div class="card__stripe"></div>
    <div class="card__stripe-tip"></div>
  </section>

</main>
</body>
</html>
```